Corvane Capital - Website Design

We need a website design for a new commercial real estate company called Corvane Capital. We're effectively commercial mortgage brokers connecting real estate investors to lenders. We need a website that is simple (not busy), elegant, professional, and user-friendly. A lot of the users will be in their 50's and less tech savvy, so a stream-lined design is best. The website will serve as a portal for lenders to review new financing opportunities, as well as for real estate investors to review terms from lenders.
Just uploaded our logo.
Target Market(s)
Commercial real estate investors and lenders
Industry/Entity Type
Real Estate
Number of Pages Required
1 page
Colors
Designer to choose colors to be used in the design.
Look and feel
Each slider illustrates characteristics of the customer's brand and the style your logo design should communicate.

```html
<!DOCTYPE html>
<html lang="en">
<head>
<meta charset="utf-8">
<title>Corvane Capital</title>
<link href="https://fonts.googleapis.com/css2?family=Cinzel:wght@400;700&family=Open+Sans:wght@400;600;700&display=swap" rel="stylesheet">
<style>
:root{
  --gold:#d5a254;
  --gold-soft:#deb46f;
  --navy:#2f4667;
  --ink:#222;
  --muted:#666;
  --line:#cfcfcf;
  --dark:#1d1d1d;
  --white:#fff;
}
*{box-sizing:border-box;margin:0;padding:0}
html,body{width:1200px;height:3000px;overflow:hidden}
body{position:relative;font-family:"Open Sans",Arial,sans-serif;color:var(--ink);background:var(--white)}
.abs{position:absolute}

/* header + hero */
.hero{left:0;top:0;width:1200px;height:560px;overflow:hidden}
.hero-photo{position:absolute;inset:0;background:
  radial-gradient(ellipse at 72% 55%,#c9a37a 0%,rgba(150,110,70,.6) 30%,transparent 60%),
  linear-gradient(180deg,#3a3a3c 0%,#6d5a48 45%,#b98a5a 75%,#8a6040 100%)}
.hero-shade{position:absolute;inset:0;background:rgba(0,0,0,.22)}
.hero-curve{position:absolute;left:0;top:0}
.brand{left:100px;top:24px;display:flex;align-items:center;gap:14px;color:var(--white)}
.brand-dot{width:58px;height:58px;border-radius:50%;background:var(--white);flex:none}
.brand-name{font-family:"Cinzel",Georgia,serif;font-size:26px;letter-spacing:1px;line-height:1;white-space:nowrap}
.topbar{right:100px;top:14px;display:flex;align-items:center;gap:26px;color:var(--white);font-size:15px}
.topbar b{font-size:19px}
.apply-top{border:2px solid var(--white);border-radius:22px;padding:6px 18px;font-weight:700;font-size:14px}
.nav{right:100px;top:70px;display:flex;gap:22px;font-family:"Cinzel",Georgia,serif;font-size:16px;color:var(--white);align-items:center;white-space:nowrap}
.nav .active{color:var(--gold)}
.hero-title{left:0;width:1200px;top:154px;text-align:center;color:var(--white);font-family:"Cinzel",Georgia,serif;font-weight:700;font-size:40px;letter-spacing:1px}
.hero-sub{left:340px;width:520px;top:216px;text-align:center;color:var(--white);font-size:21px;font-weight:600;line-height:32px}
.quote-btn{left:508px;top:302px;width:184px;height:48px;border:2px solid var(--white);border-radius:24px;color:var(--white);font-size:16px;font-weight:700;display:flex;align-items:center;justify-content:center;letter-spacing:1px}
.dots{left:568px;top:410px;display:flex;gap:6px}
.dots i{width:12px;height:12px;border-radius:50%;border:2px solid var(--white)}
.dots i.on{background:var(--white)}

/* services */
.service{top:588px;width:232px;height:252px;border:2px solid #aaa;text-align:center}
.service .ic{width:96px;height:96px;border-radius:50%;background:#efefef;margin:26px auto 0;display:flex;align-items:center;justify-content:center}
.service h3{font-family:"Cinzel",Georgia,serif;font-weight:400;font-size:20px;line-height:26px;margin-top:22px}
.service p{font-size:12.5px;color:var(--muted);line-height:24px;margin-top:6px;padding:0 16px}

/* logins */
.login{top:924px;width:600px;height:320px}
.login.client{left:0;background:var(--navy)}
.login.lender{left:600px;background:var(--gold)}
.login .ic{position:absolute;left:100px;top:48px}
.login h2{position:absolute;left:222px;top:60px;color:var(--white);font-family:"Cinzel",Georgia,serif;font-weight:700;font-size:32px}
.field{position:absolute;left:222px;width:346px;height:36px;background:var(--white);font-size:13px;color:#888;display:flex;align-items:center;gap:8px;padding-left:14px}
.submit{position:absolute;left:222px;top:220px;width:114px;height:46px;border:2px solid var(--white);border-radius:23px;color:var(--white);font-weight:700;font-size:15px;display:flex;align-items:center;justify-content:center}
.forgot{position:absolute;right:32px;top:222px;color:var(--white);font-size:12px;text-decoration:underline;font-weight:600}

/* blog */
.section-title{left:0;width:1200px;text-align:center;font-family:"Cinzel",Georgia,serif;font-weight:700;font-size:32px}
.post{top:1390px;width:312px}
.post .photo{height:210px;position:relative}
.post .date{position:absolute;left:0;top:140px;width:58px;background:var(--gold);color:var(--white);text-align:center}
.post .date b{display:block;font-size:18px;line-height:28px}
.post .date span{display:block;background:#555;font-size:11px;line-height:24px;font-weight:700}
.post h4{font-size:19px;font-weight:600;margin-top:20px}
.post p{font-size:12.5px;color:var(--muted);line-height:24px;margin-top:6px}
.post .meta{border-top:1px solid var(--line);margin-top:18px;padding-top:16px;font-size:12px;color:var(--muted);display:flex;gap:22px}

/* loan calculator */
.calc{left:0;top:1834px;width:1200px;height:424px;overflow:hidden}
.calc-photo{position:absolute;inset:0;background:linear-gradient(100deg,#5b5b5e 0%,#7d7a78 45%,#a88a62 70%,#6a6a6c 100%)}
.calc-shade{position:absolute;inset:0;background:rgba(30,30,35,.35)}
.calc-wedge{position:absolute;left:0;top:0}
.calc h2{position:absolute;left:100px;top:46px;width:330px;color:var(--white);font-family:"Cinzel",Georgia,serif;font-weight:700;font-size:31px;line-height:42px}
.calc .lead{position:absolute;left:100px;top:186px;width:260px;color:var(--white);font-size:12.5px;line-height:22px}
.calc .more{position:absolute;left:100px;top:272px;color:var(--white);font-size:13px;font-weight:700}
.calc .lbl{position:absolute;left:530px;color:var(--white);font-size:14px;line-height:18px}
.track{position:absolute;left:600px;width:260px;height:10px;border-radius:5px;background:rgba(200,200,200,.8)}
.track .fill{position:absolute;left:0;top:0;height:10px;border-radius:5px;background:#1f2f4a}
.track .knob{position:absolute;top:-5px;width:20px;height:20px;border-radius:50%;background:var(--white)}
.val{position:absolute;left:886px;width:214px;height:38px;background:var(--white);font-size:14px;padding-left:18px;display:flex;align-items:center}
.radios{position:absolute;left:530px;top:236px;display:flex;gap:46px;color:var(--white);font-size:13px}
.radios span{display:flex;align-items:center;gap:12px}
.radios i{width:13px;height:13px;border-radius:50%;border:2px solid var(--white)}
.radios i.on{background:#556;box-shadow:inset 0 0 0 2px var(--white)}
.est{position:absolute;left:530px;top:278px;color:var(--white);font-size:16px;font-weight:600}
.apply{position:absolute;left:886px;top:324px;width:138px;height:40px;border-radius:20px;background:var(--gold-soft);color:var(--white);font-weight:700;font-size:14px;display:flex;align-items:center;justify-content:center;gap:8px}

/* partners */
.partner{top:2404px;width:176px;height:84px;border:2px solid #ddd;display:flex;align-items:center;justify-content:center}
.partner i{width:120px;height:30px;background:#d6d6d6;border-radius:4px}

/* footer */
.footer{left:0;top:2530px;width:1200px;height:470px}
.f-brand{left:100px;top:2760px;display:flex;align-items:center;gap:12px;color:var(--white)}
.f-brand .brand-dot{width:50px;height:50px}
.f-brand .brand-name{font-size:22px}
.f-col{top:2696px;color:var(--white)}
.f-col h5{font-family:"Cinzel",Georgia,serif;font-weight:400;font-size:17px;letter-spacing:.5px;white-space:nowrap}
.links{list-style:none;margin-top:18px;font-size:12.5px;line-height:19.6px}
.f-col p{font-size:12.5px;line-height:22px;margin-top:18px}
.f-input{width:252px;height:34px;background:var(--white);color:#666;font-size:12px;display:flex;align-items:center;padding-left:16px;margin-top:14px}
.f-btn{display:inline-flex;align-items:center;justify-content:center;margin-top:20px;width:100px;height:28px;border-radius:14px;background:var(--gold-soft);font-size:11px;font-weight:700}
.contact{list-style:none;margin-top:18px;font-size:12.5px;line-height:22px}
.contact li{display:flex;gap:16px;margin-bottom:12px}
.contact svg{flex:none;margin-top:4px}
.f-rule{left:100px;top:2920px;width:1000px;height:1px;background:#444}
.copy{left:100px;top:2946px;color:var(--white);font-size:12px}
.social{left:978px;top:2944px;display:flex;gap:8px}
.social i{width:26px;height:26px;border-radius:50%;border:1px solid var(--white)}
</style>
</head>
<body>

<header class="abs hero">
  <div class="hero-photo" role="img" aria-label="Photo of a hand signing papers beside a small model house on a wooden desk"></div>
  <div class="hero-shade"></div>
  <svg class="hero-curve" width="1200" height="560" viewBox="0 0 1200 560">
    <path d="M0 560 L0 552 Q600 440 1200 552 L1200 560 Z" fill="#fff"/>
    <path d="M0 548 Q600 436 1200 548" fill="none" stroke="var(--gold)" stroke-width="6"/>
  </svg>
</header>

<div class="abs brand"><span class="brand-dot"></span><span class="brand-name">Corvane Capital</span></div>

<div class="abs topbar">
  <span><svg width="14" height="14" viewBox="0 0 24 24"><path d="M6 2l4 4-2 3a12 12 0 006 6l3-2 4 4-3 3C9 20 4 15 3 5z" fill="var(--gold)"/></svg>&nbsp; CALL US : <b>1 800 555 0142</b></span>
  <span class="apply-top">✎ APPLY NOW</span>
</div>

<nav class="abs nav">
  <span class="active">Home</span><span>About Us</span><span>Borrower</span><span>Lenders</span><span>Resources</span><span>Contact</span>
  <svg width="15" height="15" viewBox="0 0 24 24"><circle cx="10" cy="10" r="7" fill="none" stroke="#fff" stroke-width="3"/><path d="M15 15l7 7" stroke="#fff" stroke-width="3"/></svg>
</nav>

<h1 class="abs hero-title">WELCOME TO CORVANE CAPITAL</h1>
<p class="abs hero-sub">Providing access to hundreds of commercial real estate capital providers</p>
<div class="abs quote-btn">GET A QUOTE</div>
<div class="abs dots"><i class="on"></i><i></i><i></i><i></i></div>

<section>
  <div class="abs service" style="left:98px">
    <div class="ic"><svg width="40" height="44" viewBox="0 0 40 44"><rect x="6" y="2" width="28" height="40" fill="none" stroke="var(--gold)" stroke-width="3"/><g fill="var(--gold)"><rect x="12" y="8" width="5" height="5"/><rect x="23" y="8" width="5" height="5"/><rect x="12" y="17" width="5" height="5"/><rect x="23" y="17" width="5" height="5"/><rect x="12" y="26" width="5" height="5"/><rect x="23" y="26" width="5" height="5"/><rect x="17" y="34" width="6" height="8"/></g></svg></div>
    <h3>Construction</h3><p>Nemo enim ipsam voluptatequ ia volu ptas sit asperna</p>
  </div>
  <div class="abs service" style="left:354px">
    <div class="ic"><svg width="44" height="44" viewBox="0 0 44 44" fill="none" stroke="var(--gold)" stroke-width="5"><path d="M36 16A15 15 0 009 14"/><path d="M8 28a15 15 0 0027 2"/><path d="M30 16h8V8M14 28H6v8" stroke-width="4"/></svg></div>
    <h3>Bridge</h3><p>Nemo enim ipsam voluptatequ ia volu ptas sit asperna</p>
  </div>
  <div class="abs service" style="left:612px">
    <div class="ic"><svg width="44" height="44" viewBox="0 0 44 44"><circle cx="22" cy="22" r="20" fill="var(--gold)"/><path d="M12 22l7 7 13-14" fill="none" stroke="#fff" stroke-width="5"/></svg></div>
    <h3>Permanent</h3><p>Nemo enim ipsam voluptatequ ia volu ptas sit asperna</p>
  </div>
  <div class="abs service" style="left:868px">
    <div class="ic"><svg width="50" height="44" viewBox="0 0 50 44" fill="none" stroke="var(--gold)" stroke-width="3.5"><path d="M4 16c0-7 7-12 15-12s15 5 15 12-7 12-15 12c-2 0-4 0-6-1l-7 4 2-6c-3-2-4-5-4-9z"/><path d="M37 14c6 1 10 6 10 11 0 3-1 5-3 7l2 6-7-3c-2 1-4 1-6 1-5 0-9-2-11-5"/></svg></div>
    <h3>Advisory</h3><p>Nemo enim ipsam voluptatequ ia volu ptas sit asperna</p>
  </div>
</section>

<section>
  <div class="abs login client">
    <svg class="ic" width="92" height="88" viewBox="0 0 92 88" fill="#fff"><circle cx="46" cy="20" r="16"/><path d="M20 86c0-24 10-40 26-40s26 16 26 40z"/><circle cx="16" cy="30" r="11"/><path d="M0 76c0-18 6-28 16-28 4 0 7 1 9 3-6 8-8 16-8 25z"/><circle cx="76" cy="30" r="11"/><path d="M92 76c0-18-6-28-16-28-4 0-7 1-9 3 6 8 8 16 8 25z"/></svg>
    <h2>Client Login</h2>
    <div class="field" style="top:120px"><svg width="13" height="10" viewBox="0 0 13 10"><rect width="13" height="10" fill="#777"/><path d="M0 0l6.5 5L13 0" stroke="#fff" fill="none"/></svg>Email Address</div>
    <div class="field" style="top:166px"><svg width="10" height="12" viewBox="0 0 10 12"><rect y="5" width="10" height="7" fill="#777"/><path d="M2 5V3a3 3 0 016 0v2" stroke="#777" fill="none" stroke-width="1.6"/></svg>Password</div>
    <div class="submit">SUBMIT</div>
    <div class="forgot">Forgot Password?</div>
  </div>
  <div class="abs login lender">
    <svg class="ic" width="72" height="78" viewBox="0 0 72 78" fill="#fff" style="left:54px"><circle cx="36" cy="20" r="18"/><path d="M2 78c0-24 14-38 34-38s34 14 34 38z"/></svg>
    <h2 style="left:156px">Lender Login</h2>
    <div class="field" style="top:120px;left:156px"><svg width="13" height="10" viewBox="0 0 13 10"><rect width="13" height="10" fill="#777"/><path d="M0 0l6.5 5L13 0" stroke="#fff" fill="none"/></svg>Email Address</div>
    <div class="field" style="top:166px;left:156px"><svg width="10" height="12" viewBox="0 0 10 12"><rect y="5" width="10" height="7" fill="#777"/><path d="M2 5V3a3 3 0 016 0v2" stroke="#777" fill="none" stroke-width="1.6"/></svg>Password</div>
    <div class="submit" style="left:156px">SUBMIT</div>
    <div class="forgot">Forgot Password?</div>
  </div>
</section>

<h2 class="abs section-title" style="top:1308px">LATEST BLOG</h2>
<section>
  <article class="abs post" style="left:98px">
    <div class="photo" role="img" aria-label="Photo of a smiling man working on a laptop in a bright office" style="background:linear-gradient(135deg,#e8ecef,#b9c4cf 55%,#6f8aa6)"><div class="date"><b>02</b><span>AUG</span></div></div>
    <h4>Finibus Bonorum et Malorum</h4>
    <p>Nam libero tempore, cum soluta nobis est eligendi optio cumque nihil impedit quo minus id qu..</p>
    <div class="meta"><span>👤 Ellen Hart</span><span>💬 3 Comments</span></div>
  </article>
  <article class="abs post" style="left:442px">
    <div class="photo" role="img" aria-label="Photo of hands with a pen and calculator over printed charts on a desk" style="background:linear-gradient(135deg,#8a7a62,#d9d4cc 40%,#5fa0c8 70%,#c9b79a)"><div class="date"><b>02</b><span>AUG</span></div></div>
    <h4>Finibus Bonorum et Malorum</h4>
    <p>Nam libero tempore, cum soluta nobis est eligendi optio cumque nihil impedit quo minus id qu..</p>
    <div class="meta"><span>👤 Ellen Hart</span><span>💬 3 Comments</span></div>
  </article>
  <article class="abs post" style="left:788px">
    <div class="photo" role="img" aria-label="Photo of a woman using a calculator next to a laptop" style="background:linear-gradient(135deg,#3a2a24,#8a5a44 45%,#d8d2cc 80%,#f0eeec)"><div class="date"><b>02</b><span>AUG</span></div></div>
    <h4>Finibus Bonorum et Malorum</h4>
    <p>Nam libero tempore, cum soluta nobis est eligendi optio cumque nihil impedit quo minus id qu..</p>
    <div class="meta"><span>👤 Ellen Hart</span><span>💬 3 Comments</span></div>
  </article>
</section>

<section class="abs calc">
  <div class="calc-photo" role="img" aria-label="Photo of hands typing on a laptop keyboard in warm light"></div>
  <div class="calc-shade"></div>
  <svg class="calc-wedge" width="1200" height="424" viewBox="0 0 1200 424"><path d="M0 0H580L184 424 0 230Z" fill="var(--gold)" opacity=".95"/></svg>
  <h2>How much would you like to borrow?</h2>
  <p class="lead">Nemo enim ipsam voluptatem quia volu ptas sit aspernatur aut odit aut fugit, sed quia consequuntur magni.</p>
  <div class="more">READ MORE &gt;&gt;</div>

  <div class="lbl" style="top:62px">Loan<br>Amount</div>
  <div class="track" style="top:80px"><div class="fill" style="width:60px"></div><div class="knob" style="left:50px"></div></div>
  <div class="val" style="top:62px">$20000</div>

  <div class="lbl" style="top:114px">Interest<br>Rate</div>
  <div class="track" style="top:132px"><div class="fill" style="width:36px"></div><div class="knob" style="left:26px"></div></div>
  <div class="val" style="top:114px">10%</div>

  <div class="lbl" style="top:166px">Loan<br>Term</div>
  <div class="track" style="top:184px"><div class="fill" style="width:190px"></div><div class="knob" style="left:180px"></div></div>
  <div class="val" style="top:166px">7 Years</div>

  <div class="radios"><span><i class="on"></i>Monthly</span><span><i></i>Fortnightly</span><span><i></i>Weekly</span></div>
  <div class="est">Your Estimated Repayments Would be:</div>
  <div class="val" style="top:270px">$73.98</div>
  <div class="apply">✎ APPLY NOW</div>
</section>

<h2 class="abs section-title" style="top:2328px">OUR PARTNERS</h2>
<section>
  <div class="abs partner" style="left:98px"><i></i></div>
  <div class="abs partner" style="left:306px"><i></i></div>
  <div class="abs partner" style="left:512px"><i></i></div>
  <div class="abs partner" style="left:720px"><i></i></div>
  <div class="abs partner" style="left:926px"><i></i></div>
</section>

<footer>
  <svg class="abs footer" width="1200" height="470" viewBox="0 0 1200 470">
    <path d="M0 0Q600 170 1200 0V470H0Z" fill="var(--dark)"/>
    <path d="M0 6Q600 176 1200 6" fill="none" stroke="var(--gold)" stroke-width="6"/>
  </svg>
  <div class="abs f-brand"><span class="brand-dot"></span><span class="brand-name">Corvane Capital</span></div>
  <div class="abs f-col" style="left:424px">
    <h5>QUICK LINKS</h5>
    <ul class="links"><li>Home</li><li>About Us</li><li>Marketplace</li><li>Broker</li><li>Lenders</li><li>Resources</li><li>Blog</li><li>Contact</li></ul>
  </div>
  <div class="abs f-col" style="left:576px;width:260px">
    <h5>NEWSLETTER SUBSCRIPTION</h5>
    <p>Register your Email Address to get information about us</p>
    <div class="f-input">Email Address</div>
    <span class="f-btn">SUBSCRIBE</span>
  </div>
  <div class="abs f-col" style="left:880px;width:240px">
    <h5>CONTACT US</h5>
    <ul class="contact">
      <li><svg width="10" height="14" viewBox="0 0 10 14"><path d="M5 0a5 5 0 015 5c0 4-5 9-5 9S0 9 0 5a5 5 0 015-5z" fill="#fff"/><circle cx="5" cy="5" r="2" fill="var(--dark)"/></svg>Veldstraat 12, 4801 AB Breda Nederland</li>
      <li><svg width="12" height="12" viewBox="0 0 24 24"><path d="M6 2l4 4-2 3a12 12 0 006 6l3-2 4 4-3 3C9 20 4 15 3 5z" fill="#fff"/></svg>1 800 555 0142</li>
      <li><svg width="13" height="10" viewBox="0 0 13 10"><rect width="13" height="10" fill="#fff"/><path d="M0 0l6.5 5L13 0" stroke="var(--dark)" fill="none"/></svg>info@corvanecapital.com</li>
    </ul>
  </div>
  <div class="abs f-rule"></div>
  <div class="abs copy">Copyrights © 2017, Corvane Capital. &nbsp;All rights reserved.</div>
  <div class="abs social"><i></i><i></i><i></i><i></i></div>
</footer>

</body>
</html>
```